Bref créative
brook gate realty business card
Simple
Miles Vetcher
Licensed Real Estate Broker
2385 West 9th Avenue
Brooklyn, NY 11230
brookgaterealtyny@quorvana.com
www.bgrny.com
front should be standard and simple
the logo in a corner and small or in the back ground.
logo with a clean black or white setting. possibly with borders
i want the card to portray power and elegance.
i uploaded the complete zip file from tavelink if this is to much please tell me and ill changeit.

```html
<!DOCTYPE html>
<html lang="en">
<head>
<meta charset="utf-8">
<title>Brook Gate Realty – Business Card</title>
<link rel="stylesheet" href="https://fonts.googleapis.com/css2?family=Cinzel:wght@600&family=Open+Sans:wght@400;700&display=swap">
<style>
  :root {
    --backdrop: #3b3835;
    --card-light: #ffffff;
    --card-shade: #e4e4e4;
    --ink: #2b2b2b;
    --ink-soft: #6a6a6a;
    --mark: #5c5c5c;
    --rule: #b9b9b9;
  }
  * { box-sizing: border-box; margin: 0; padding: 0; }
  html, body {
    width: 1200px; height: 667px; overflow: hidden;
    background: var(--backdrop);
  }
  .canvas { position: relative; width: 1200px; height: 667px; }
  .card {
    position: absolute;
    border-radius: 12px;
    background: linear-gradient(160deg, var(--card-light) 0%, var(--card-light) 45%, var(--card-shade) 100%);
    box-shadow: 0 6px 18px rgba(0,0,0,.45);
  }
  .card--front { left: 168px; top: 115px; width: 461px; height: 257px; z-index: 2; }
  .card--back  { left: 492px; top: 264px; width: 511px; height: 293px; z-index: 1; }

  .brand { position: absolute; left: 60px; top: 38px; width: 170px; }
  .brand__square { width: 34px; height: 34px; background: var(--mark); margin-left: 4px; }
  .brand__name {
    margin-top: 10px;
    font-family: "Cinzel", serif; font-weight: 600;
    font-size: 15px; letter-spacing: .5px; color: var(--ink);
    white-space: nowrap;
  }
  .brand__tagline {
    margin-top: 2px;
    font-family: "Open Sans", sans-serif; font-size: 5.5px;
    letter-spacing: .8px; text-transform: uppercase; color: var(--ink-soft);
    white-space: nowrap;
  }

  .person__marker { position: absolute; left: 0; top: 127px; width: 14px; height: 20px; background: var(--ink); }
  .person { position: absolute; left: 34px; top: 127px; font-family: "Open Sans", sans-serif; }
  .person__name { font-weight: 700; font-size: 10.5px; color: var(--ink); }
  .person__title { font-size: 7px; color: var(--ink-soft); margin-top: 1px; }
  .person__rule { position: absolute; left: 34px; top: 162px; width: 380px; height: 1px; background: var(--rule); }

  .contact {
    position: absolute; top: 184px;
    font-family: "Open Sans", sans-serif; font-size: 6.5px; line-height: 1.55;
    color: var(--ink);
  }
  .contact--address { left: 34px; }
  .contact--lines { left: 156px; padding-left: 10px; border-left: 1px solid var(--rule); }
  .contact__sep { color: var(--rule); margin: 0 5px; }
  .contact--web { left: 34px; top: 222px; }

  .back-brand {
    position: absolute; left: 130px; top: 118px;
    display: flex; align-items: center; gap: 12px;
  }
  .back-brand__square { width: 44px; height: 44px; background: var(--mark); }
  .back-brand__name {
    font-family: "Cinzel", serif; font-weight: 600;
    font-size: 22px; letter-spacing: 1px; color: var(--mark);
    white-space: nowrap;
  }
</style>
</head>
<body>
<main class="canvas">
  <section class="card card--front" aria-label="Card front">
    <div class="brand">
      <div class="brand__square"></div>
      <div class="brand__name">BROOK GATE REALTY</div>
      <div class="brand__tagline">Brokerage &amp; Management Solutions</div>
    </div>

    <div class="person__marker"></div>
    <div class="person">
      <div class="person__name">Miles Vetcher</div>
      <div class="person__title">Licensed Real Estate Broker</div>
    </div>
    <div class="person__rule"></div>

    <div class="contact contact--address">
      2385 West 9th Avenue<br>
      Brooklyn, NY 11230
    </div>
    <div class="contact contact--lines">
      Phone: 718-555-0142<span class="contact__sep">|</span>Cell: 917-555-0198<br>
      Fax: 866-555-0163<span class="contact__sep">|</span>Email: brookgaterealtyny@quorvana.com
    </div>
    <div class="contact contact--web">www.bgrny.com</div>
  </section>

  <section class="card card--back" aria-label="Card back">
    <div class="back-brand">
      <div class="back-brand__square"></div>
      <div class="back-brand__name">BROOK GATE REALTY</div>
    </div>
  </section>
</main>
</body>
</html>
```